ClinicorNest Magazine Design for a digital monthly magazine

Designing an online magazine for monthly distribution. The magazine will be related to topics that are important to physicians. Finance, family, self-employment, medications, supplies, residency, continuing education, trends, advances, technology, etc. An example of another company that writes a monthly medical digital magazine editorial is Velbrook Medical Post. Here is a link to one of their editions. https://pagevane.example/velbrookmedicalpost/docs/vmp_april2021?fr=kQzPwR7tYbN2LdXa I want our project to be more modern looking, less busy, and much more friendly to the eye. We have a website design project in process through ArtisQuarry currently. I've spliced together some of our favorite parts of the designs that were submitted so far so you can have a vision for the theme, colors, and logos.
I’m looking for a template for the cover and inside page layout.

Target Market(s)

Physicians

Industry/Entity Type

Medical

Font styles to use
Other font styles liked:
• Rubik

Colors
0054AA
0677BA
7BADD7
CADEEF
E8F1F8
59FF00
82FF00
B8FF75
E3FFCB
F4FFEA

Requirements
Must have
• Project must be centered around Physicians. Discusses topics that are physician centric. Finance, family, medical supplies, insurance, billing, technology, private practice, employed practice, etc.
Nice to have
• The ability to create a 15 - 20 page monthly editorial from the design theme and structure that you create
Should not have
• should not bee to busy and flat looking. Must be modern and welcoming to the eye

```html
<!DOCTYPE html>
<html lang="en">
<head>
<meta charset="utf-8">
<title>ClinicorNest Magazine – Cover and Inside Page Templates</title>
<link href="https://fonts.googleapis.com/css2?family=Rubik:wght@300;400;500;700&display=swap" rel="stylesheet">
<style>
:root{
  --blue:#0054AA;
  --blue-mid:#0677BA;
  --sky:#7BADD7;
  --mist:#CADEEF;
  --ice:#E8F1F8;
  --lime:#59FF00;
  --lime-soft:#82FF00;
  --ink:#555a60;
  --canvas:#efefef;
  --white:#ffffff;
}
*{box-sizing:border-box;margin:0;padding:0}
html,body{width:1200px;height:4285px;overflow:hidden}
body{background:var(--canvas);font-family:"Rubik",sans-serif;position:relative;color:var(--ink)}
.page{position:absolute;width:565px;height:800px;background:var(--white);overflow:hidden}
.abs{position:absolute}
.photo{position:absolute}
.head{font-weight:700;font-size:12px;line-height:15px;color:var(--blue);text-transform:uppercase;margin-bottom:12px}
.head.light{color:var(--white)}
.section-title{position:absolute;font-weight:300;font-size:19px;color:#4d5156;text-transform:uppercase;letter-spacing:.2px}
.body{font-size:10.4px;line-height:13.6px;color:var(--ink);overflow:hidden}
.body.light{color:var(--white)}
.col{position:absolute;width:212px}
.col.wide{width:210px}
.checklist{list-style:none}
.checklist li{display:flex;gap:8px;font-size:10.4px;line-height:13.6px;margin-bottom:11px}
.checklist svg{flex:none;margin-top:1px}
.bullets{list-style:none}
.bullets li{position:relative;padding-left:17px;font-size:10.4px;line-height:13.6px;margin-bottom:19px}
.bullets li::before{content:"";position:absolute;left:2px;top:5px;width:4px;height:4px;border-radius:50%;background:var(--ink)}
.arrows{list-style:none}
.arrows li{position:relative;padding-left:12px;font-size:10.4px;line-height:13px;color:var(--white);margin-bottom:7px}
.arrows li::before{content:"›";position:absolute;left:0;top:-1px;font-size:14px}
.stat{position:absolute;width:70px;height:70px;border:3px solid var(--white);border-radius:50%;display:flex;align-items:center;justify-content:center;font-weight:700;font-size:23px;color:var(--white)}
</style>
</head>
<body>

<!-- Cover -->
<section class="page cover" style="left:600px;top:60px;width:564px">
  <div class="photo" role="img" aria-label="Stethoscope beside a red heart and a clipboard on a pale desk" style="left:0;top:0;width:564px;height:600px;background:linear-gradient(135deg,#e9ebf3 0%,#d7dbe6 45%,#c9ccd6 100%)"></div>
  <div class="abs brand" style="left:52px;top:80px;display:flex;align-items:center;gap:8px">
    <span style="width:26px;height:26px;border-radius:50%;background:var(--blue)"></span>
    <span style="font-weight:700;font-size:11px;color:var(--blue);letter-spacing:.3px">CLINICORNEST</span>
  </div>
  <svg class="abs" style="left:0;top:0" width="564" height="800" viewBox="0 0 564 800">
    <polygon points="0,556 240,556 250,522 258,600 266,586 564,586 564,800 0,800" fill="#0054AA"/>
    <polyline points="0,556 240,556 250,522 258,600 266,586 564,586" fill="none" stroke="#59FF00" stroke-width="3" stroke-linejoin="round"/>
  </svg>
  <h1 class="abs" style="left:62px;top:660px;font-weight:700;font-size:21px;color:var(--white);text-transform:uppercase">Lorem Ipsum Dolor Sit Amet</h1>
  <p class="abs" style="left:62px;top:692px;font-size:13px;color:var(--white)">Lorem Ipsum Dolor Sit Amet Consectetuer</p>
</section>

<!-- Spread 1 left -->
<section class="page" style="left:35px;top:892px">
  <div class="photo" role="img" aria-label="Scientist in protective gear working at a microscope" style="left:0;top:0;width:565px;height:318px;background:linear-gradient(120deg,#2b5e9a 0%,#7fa6d2 45%,#dfe9f4 100%)"></div>
  <div class="abs" style="left:32px;top:90px;width:246px;height:183px;background:var(--blue-mid);padding:22px 28px">
    <p class="body light">Lorem ipsum dolor sit amet, consect adipiscing elit, sed diam nonummy nibh euismod tincidunt ut laoreet dol magna aliquam erat volutpat. Ut wisi enim ad minim veniam, quis nostrud exerci tation ullamcorper suscipit lob nisl ut aliquip ex ea commodo cons. Duis autem vel eum iriure dolor inum hendrerit in vulputate velit esse mole</p>
  </div>
  <h2 class="section-title" style="left:63px;top:350px">Lorem Ipsum Dolor Sit Amet</h2>
  <div class="col" style="left:63px;top:408px">
    <h3 class="head">Lorem Ipsum Dolor Sit<br>Amet Consectetuer</h3>
    <p class="body" style="height:286px">Lorem ipsum dolor sit amet, consect adipiscing elit, sed diam nonummy nibh euismod tincidunt ut laoreet dol magna aliquam erat volutpat. Ut wisi enim ad minim veniam, quis nostrud exerci tation ullamcorper suscipit lob nisl ut aliquip ex ea commodo cons. Duis autem vel eum iriure dolor inum hendrerit in vulputate velit esse mole consequat, vel illum dolore eu feugia nulla facilisis at vero eros et accums et iusto odio dignissim qui blandit pr luptatum zzril delenit augue duis dol te feugait nulla facilisi. Lorem ipsum dolor sit amet, cons ectetuer adipisci elit, sed diam nonummy nibh euismo tincidunt ut laoreet dolore magna ali erat volutpat. Ut wisi enim ad minim veniam, quis nostrud exerci tation ull suscipit lobortis nisl ut aliquip ex ean commodo consequat.</p>
  </div>
  <div class="col" style="left:318px;top:408px">
    <h3 class="head">Lorem Ipsum Dolor Sit<br>Amet Consectetuer</h3>
    <p class="body" style="height:286px">Lorem ipsum dolor sit amet, consect adipiscing elit, sed diam nonummy nibh euismod tincidunt ut laoreet dol magna aliquam erat volutpat. Ut wisi enim ad minim veniam, quis nostrud exerci tation ullamcorper suscipit lob nisl ut aliquip ex ea commodo cons. Duis autem vel eum iriure dolor inum hendrerit in vulputate velit esse mole consequat, vel illum dolore eu feugia nulla facilisis at vero eros et accums et iusto odio dignissim qui blandit pr luptatum zzril delenit augue duis dol te feugait nulla facilisi. Lorem ipsum dolor sit amet, cons ectetuer adipisci elit, sed diam nonummy nibh euismo tincidunt ut laoreet dolore magna ali erat volutpat. Ut wisi enim ad minim veniam, quis nostrud exerci tation ull suscipit lobortis nisl ut aliquip ex ean commodo consequat.</p>
  </div>
</section>

<!-- Spread 1 right -->
<section class="page" style="left:600px;top:892px">
  <div class="photo" role="img" aria-label="Surgical team in masks and loupes during an operation" style="left:0;top:0;width:565px;height:128px;background:linear-gradient(90deg,#123a55 0%,#2d6d86 50%,#17455e 100%)"></div>
  <div class="col" style="left:62px;top:167px;width:200px">
    <h3 class="head">Lorem Ipsum Dolor Sit<br>Amet Consectetuer</h3>
    <p class="body" style="height:96px;margin-bottom:14px">Lorem ipsum dolor sit amet, consect adipiscing elit, sed diam nonummy nibh euismod tincidunt ut laoreet dol magna aliquam erat volutpat. Ut wisi enim ad minim veniam, quis nostrud exerci tation ullamcorper suscipit lob nisl ut aliquip ex ea commodo cons.</p>
    <ul class="checklist">
      <li><svg width="12" height="12" viewBox="0 0 12 12"><circle cx="6" cy="6" r="5" fill="none" stroke="#0677BA" stroke-width="1.2"/><path d="M3.5 6.2l1.7 1.7 3.3-3.4" fill="none" stroke="#0677BA" stroke-width="1.2"/></svg><span>Lorem ipsum dolor sit amet com adipiscing elit sed diam nonumu</span></li>
      <li><svg width="12" height="12" viewBox="0 0 12 12"><circle cx="6" cy="6" r="5" fill="none" stroke="#0677BA" stroke-width="1.2"/><path d="M3.5 6.2l1.7 1.7 3.3-3.4" fill="none" stroke="#0677BA" stroke-width="1.2"/></svg><span>Lorem ipsum dolor sit amet com adipiscing elit sed diam nonumu</span></li>
      <li><svg width="12" height="12" viewBox="0 0 12 12"><circle cx="6" cy="6" r="5" fill="none" stroke="#0677BA" stroke-width="1.2"/><path d="M3.5 6.2l1.7 1.7 3.3-3.4" fill="none" stroke="#0677BA" stroke-width="1.2"/></svg><span>Lorem ipsum dolor sit amet com adipiscing elit sed diam nonumu</span></li>
      <li><svg width="12" height="12" viewBox="0 0 12 12"><circle cx="6" cy="6" r="5" fill="none" stroke="#0677BA" stroke-width="1.2"/><path d="M3.5 6.2l1.7 1.7 3.3-3.4" fill="none" stroke="#0677BA" stroke-width="1.2"/></svg><span>Lorem ipsum dolor sit amet com adipiscing elit sed diam nonumu</span></li>
      <li><svg width="12" height="12" viewBox="0 0 12 12"><circle cx="6" cy="6" r="5" fill="none" stroke="#0677BA" stroke-width="1.2"/><path d="M3.5 6.2l1.7 1.7 3.3-3.4" fill="none" stroke="#0677BA" stroke-width="1.2"/></svg><span>Lorem ipsum dolor sit amet com adipiscing elit sed diam nonumu</span></li>
    </ul>
  </div>
  <div class="abs" style="left:290px;top:128px;width:237px;height:394px;background:var(--blue);padding:39px 22px 0 26px">
    <h3 class="head light">Lorem Ipsum Dolor Sit<br>Amet Consectetuer</h3>
    <p class="body light" style="height:258px">Lorem ipsum dolor sit amet, consect adipiscing elit, sed diam nonummy nibh euismod tincidunt ut laoreet dol magna aliquam erat volutpat. Ut wisi enim ad minim veniam, quis nostrud exerci tation ullamcorper suscipit lob nisl ut aliquip ex ea commodo cons. Duis autem vel eum iriure dolor inum hendrerit in vulputate velit esse mole consequat, vel illum dolore eu feugia nulla facilisis at vero eros et accums et iusto odio dignissim qui blandit pr luptatum zzril delenit augue duis dol te feugait nulla facilisi. Lorem ipsum dolor sit amet, cons ectetuer adipisci elit, sed diam nonummy nibh euismo tincidunt ut laoreet dolore magna ali erat volutpat. Ut wisi enim ad minim veniam, quis nostrud exerci tation ull</p>
  </div>
  <div class="photo" role="img" aria-label="Glowing blue DNA double helix" style="left:0;top:522px;width:290px;height:233px;background:radial-gradient(circle at 45% 50%,#4fa3e0 0%,#16508f 45%,#0a2350 100%)"></div>
  <div class="col" style="left:316px;top:548px;width:215px">
    <h3 class="head">Lorem Ipsum Dolor Sit<br>Amet Consectetuer</h3>
    <p class="body" style="height:176px">Lorem ipsum dolor sit amet, consect adipiscing elit, sed diam nonummy nibh euismod tincidunt ut laoreet dol magna aliquam erat volutpat. Ut wisi enim ad minim veniam, quis nostrud exerci tation ullamcorper suscipit lob nisl ut aliquip ex ea commodo cons. Duis autem vel eum iriure dolor inum hendrerit in vulputate velit esse mole consequat, vel illum dolore eu feugia nulla facilisis at vero eros et accums et iusto odio dignissim qui blandit pr</p>
  </div>
</section>

<!-- Spread 2 left -->
<section class="page" style="left:35px;top:1742px">
  <div class="photo" role="img" aria-label="Soft light background with faint molecular pattern" style="left:0;top:0;width:565px;height:338px;background:linear-gradient(100deg,#dbe9f3 0%,#f3f7fb 50%,#ffffff 100%)"></div>
  <div class="photo" role="img" aria-label="Portrait of a senior physician in a white coat" style="left:65px;top:66px;width:80px;height:80px;border-radius:50%;border:3px solid var(--white);background:linear-gradient(160deg,#e4e8ee 0%,#b9c4d1 100%);z-index:2"></div>
  <div class="abs" style="left:148px;top:75px;width:354px;height:80px;background:var(--blue);padding:14px 0 0 47px">
    <h3 class="head light" style="margin-bottom:6px">Lorem Ipsum Dolor Sit</h3>
    <p class="body light">Lorem ipsum dolor sit amet consect<br>Lorem ipsum dolor sit amet consect</p>
  </div>
  <p class="body abs" style="left:63px;top:184px;width:212px;height:124px">Lorem ipsum dolor sit amet, consect adipiscing elit, sed diam nonummy nibh euismod tincidunt ut laoreet dol magna aliquam erat volutpat. Ut wisi enim ad minim veniam, quis nostrud exerci tation ullamcorper suscipit lob nisl ut aliquip ex ea commodo cons. Duis autem vel eum iriure dolor inum hendrerit in vulputate velit esse mole</p>
  <p class="body abs" style="left:318px;top:184px;width:212px;height:124px">Lorem ipsum dolor sit amet, consect adipiscing elit, sed diam nonummy nibh euismod tincidunt ut laoreet dol magna aliquam erat volutpat. Ut wisi enim ad minim veniam, quis nostrud exerci tation ullamcorper suscipit lob nisl ut aliquip ex ea commodo cons. Duis autem vel eum iriure dolor inum hendrerit in vulputate velit esse mole</p>
  <div class="abs" style="left:0;top:341px;width:565px;height:172px;background:var(--blue);padding:25px 40px 0 63px">
    <h3 class="head light">Lorem Ipsum Dolor Sit</h3>
    <p class="body light">Lorem ipsum dolor sit amet, consect adipiscing elit, sed diam nonummy nibh euismod tincidunt ut laoreet dol magna aliquam erat volutpat. Ut wisi enim ad minim veniam, quis nostrud exerci tation ullamcorper suscipit lob nisl ut aliquip ex ea commodo cons. Duis autem vel eum iriure dolor inum hendrerit in vulputate velit esse mole consequat, vel illum dolore eu feugia nulla facilisis at vero eros et accums et iusto odio dignissim qui</p>
  </div>
  <div class="col" style="left:63px;top:542px">
    <h3 class="head">Lorem Ipsum Dolor Sit<br>Amet Consectetuer</h3>
    <p class="body" style="height:150px">Lorem ipsum dolor sit amet, consect adipiscing elit, sed diam nonummy nibh euismod tincidunt ut laoreet dol magna aliquam erat volutpat. Ut wisi enim ad minim veniam, quis nostrud exerci tation ullamcorper suscipit lob nisl ut aliquip ex ea commodo cons. Duis autem vel eum iriure dolor inum hendrerit in vulputate velit esse mole consequat, vel illum dolore eu feugia nulla facilisis at vero eros et accums</p>
  </div>
  <div class="col" style="left:318px;top:542px">
    <h3 class="head">Lorem Ipsum Dolor Sit<br>Amet Consectetuer</h3>
    <p class="body" style="height:150px">Lorem ipsum dolor sit amet, consect adipiscing elit, sed diam nonummy nibh euismod tincidunt ut laoreet dol magna aliquam erat volutpat. Ut wisi enim ad minim veniam, quis nostrud exerci tation ullamcorper suscipit lob nisl ut aliquip ex ea commodo cons. Duis autem vel eum iriure dolor inum hendrerit in vulputate velit esse mole consequat, vel illum dolore eu feugia nulla facilisis at vero eros et accums</p>
  </div>
</section>

<!-- Spread 2 right -->
<section class="page" style="left:600px;top:1742px">
  <div class="photo" role="img" aria-label="Blue tinted laboratory test tubes and vials" style="left:0;top:0;width:290px;height:800px;background:linear-gradient(170deg,#2f74b4 0%,#4d8fc6 40%,#3a7cb9 70%,#5b9bd0 100%)"></div>
  <div class="col" style="left:62px;top:62px;width:200px">
    <h3 class="head light">Lorem Ipsum Dolor Sit<br>Amet Consectetuer</h3>
    <p class="body light" style="height:164px">Lorem ipsum dolor sit amet, consect adipiscing elit, sed diam nonummy nibh euismod tincidunt ut laoreet dol magna aliquam erat volutpat. Ut wisi enim ad minim veniam, quis nostrud exerci tation ullamcorper suscipit lob nisl ut aliquip ex ea commodo cons. Duis autem vel eum iriure dolor inum hendrerit in vulputate velit esse mole consequat, vel illum dolore eu feugia nulla facilisis at vero eros et accums et iusto odio dignissim qui blandit pr</p>
  </div>
  <div class="stat" style="left:121px;top:303px">22%</div>
  <p class="body light abs" style="left:62px;top:388px;width:200px">Lorem ipsum dolor sit amet, consect adipiscing elit, sed diam nonummy nibh euismod tincidunt ut laoreet dol</p>
  <div class="stat" style="left:121px;top:458px">56%</div>
  <p class="body light abs" style="left:62px;top:543px;width:200px">Lorem ipsum dolor sit amet, consect adipiscing elit, sed diam nonummy nibh euismod tincidunt ut laoreet dol</p>
  <div class="stat" style="left:121px;top:614px">66%</div>
  <p class="body light abs" style="left:62px;top:699px;width:200px">Lorem ipsum dolor sit amet, consect adipiscing elit, sed diam nonummy nibh euismod tincidunt ut laoreet dol</p>
  <div class="col" style="left:316px;top:62px;width:215px">
    <h3 class="head">Lorem Ipsum Dolor Sit<br>Amet Consectetuer</h3>
    <p class="body" style="height:164px">Lorem ipsum dolor sit amet, consect adipiscing elit, sed diam nonummy nibh euismod tincidunt ut laoreet dol magna aliquam erat volutpat. Ut wisi enim ad minim veniam, quis nostrud exerci tation ullamcorper suscipit lob nisl ut aliquip ex ea commodo cons. Duis autem vel eum iriure dolor inum hendrerit in vulputate velit esse mole consequat, vel illum dolore eu feugia nulla facilisis at vero eros et accums et iusto odio dignissim qui blandit pr</p>
  </div>
  <div class="photo" role="img" aria-label="Researcher in a protective suit using a microscope" style="left:316px;top:304px;width:249px;height:214px;background:linear-gradient(135deg,#eef2f6 0%,#c7d3df 55%,#8fa6bd 100%)"></div>
  <div class="col" style="left:316px;top:546px;width:215px">
    <p class="body" style="height:68px;margin-bottom:14px">Lorem ipsum dolor sit amet, consect adipiscing elit, sed diam nonummy nibh euismod tincidunt ut laoreet dol magna aliquam erat volutpat. Ut wisi enim ad minim veniam, quis nostrud</p>
    <p class="body" style="height:110px">Lorem ipsum dolor sit amet, consect adipiscing elit, sed diam nonummy nibh euismod tincidunt ut laoreet dol magna aliquam erat volutpat. Ut wisi enim ad minim veniam, quis nostrud exerci tation ullamcorper suscipit lob nisl ut aliquip ex ea commodo cons. Duis autem vel eum iriure dolor inum</p>
  </div>
</section>

<!-- Spread 3 left -->
<section class="page" style="left:35px;top:2588px">
  <div class="photo" role="img" aria-label="Hands forming a roof over a paper family cut-out standing on grass" style="left:0;top:0;width:565px;height:378px;background:linear-gradient(180deg,#f2f2f0 0%,#e4e2dc 60%,#7fb34a 85%,#4f8f2a 100%)"></div>
  <div class="photo" role="img" aria-label="Nurse attending to a patient in a hospital ward" style="left:63px;top:408px;width:218px;height:136px;background:linear-gradient(135deg,#d5e3ef 0%,#7ea6c8 60%,#2f6a9c 100%)"></div>
  <div class="col" style="left:318px;top:403px">
    <h3 class="head">Lorem Ipsum Dolor Sit<br>Amet Consectetuer</h3>
    <p class="body" style="height:96px">Lorem ipsum dolor sit amet, consect adipiscing elit, sed diam nonummy nibh euismod tincidunt ut laoreet dol magna aliquam erat volutpat. Ut wisi enim ad minim veniam, quis nostrud exerci tation ullamcorper suscipit lob nisl ut aliquip ex ea commodo cons.</p>
  </div>
  <div class="col" style="left:63px;top:597px">
    <h3 class="head">Lorem Ipsum Dolor Sit<br>Amet Consectetuer</h3>
    <p class="body" style="height:96px">Lorem ipsum dolor sit amet, consect adipiscing elit, sed diam nonummy nibh euismod tincidunt ut laoreet dol magna aliquam erat volutpat. Ut wisi enim ad minim veniam, quis nostrud exerci tation ullamcorper suscipit lob nisl ut aliquip ex ea commodo cons.</p>
  </div>
  <div class="photo" role="img" aria-label="Medical team meeting in a conference room with screens" style="left:283px;top:602px;width:218px;height:138px;background:linear-gradient(135deg,#e3edf5 0%,#9dbbd6 55%,#3e6f99 100%)"></div>
</section>

<!-- Spread 3 right -->
<section class="page" style="left:600px;top:2588px">
  <div class="col" style="left:62px;top:62px;width:205px">
    <h3 class="head">Lorem Ipsum Dolor Sit<br>Amet Consectetuer</h3>
    <p class="body" style="height:164px;margin-bottom:14px">Lorem ipsum dolor sit amet, consect adipiscing elit, sed diam nonummy nibh euismod tincidunt ut laoreet dol magna aliquam erat volutpat. Ut wisi enim ad minim veniam, quis nostrud exerci tation ullamcorper suscipit lob nisl ut aliquip ex ea commodo cons. Duis autem vel eum iriure dolor inum hendrerit in vulputate velit esse mole consequat, vel illum dolore eu feugia nulla facilisis at vero eros et accums et iusto odio dignissim qui blandit pr</p>
    <ul class="bullets">
      <li>Lorem ipsum dolor sit amet, cons adipiscing elit, sed diam nonumin nibh euismod tincidunt ut laoreet dol magna aliquam erat volutpat. Ut wisi enim ad minim veniam, qu nostrud exerci tation ullamcorper</li>
      <li>Lorem ipsum dolor sit amet, cons adipiscing elit, sed diam nonumin nibh euismod tincidunt ut laoreet dol magna aliquam erat volutpat. Ut wisi enim ad minim veniam, qu nostrud exerci tation ullamcorper</li>
      <li>Lorem ipsum dolor sit amet, cons adipiscing elit, sed diam nonumin nibh euismod tincidunt ut laoreet dol magna aliquam erat volutpat. Ut wisi enim ad minim veniam, qu nostrud exerci tation ullamcorper</li>
    </ul>
    <p class="body" style="height:136px;margin-top:4px">Lorem ipsum dolor sit amet, consect adipiscing elit, sed diam nonummy nibh euismod tincidunt ut laoreet dol magna aliquam erat volutpat. Ut wisi enim ad minim veniam, quis nostrud exerci tation ullamcorper suscipit lob nisl ut aliquip ex ea commodo cons. Duis autem vel eum iriure dolor inum hendrerit in vulputate velit esse mole consequat, vel illum dolore eu feugia</p>
  </div>
  <div class="col" style="left:316px;top:62px;width:215px">
    <h3 class="head">Lorem Ipsum Dolor Sit<br>Amet Consectetuer</h3>
    <p class="body" style="height:272px">Lorem ipsum dolor sit amet, consect adipiscing elit, sed diam nonummy nibh euismod tincidunt ut laoreet dol magna aliquam erat volutpat. Ut wisi enim ad minim veniam, quis nostrud exerci tation ullamcorper suscipit lob nisl ut aliquip ex ea commodo cons. Duis autem vel eum iriure dolor inum hendrerit in vulputate velit esse mole consequat, vel illum dolore eu feugia nulla facilisis at vero eros et accums et iusto odio dignissim qui blandit pr luptatum zzril delenit augue duis dol te feugait nulla facilisi. Lorem ipsum dolor sit amet, cons ectetuer adipisci elit, sed diam nonummy nibh euismo tincidunt ut laoreet dolore magna ali erat volutpat. Ut wisi enim ad minim veniam, quis nostrud exerci tation ull</p>
  </div>
  <div class="photo" role="img" aria-label="Senior doctor in a white coat reading a tablet" style="left:265px;top:391px;width:300px;height:409px;background:linear-gradient(160deg,#ffffff 0%,#e7eef6 45%,#b8c9db 100%)"></div>
</section>

<!-- Spread 4 left -->
<section class="page" style="left:35px;top:3441px">
  <div class="photo" role="img" aria-label="Diverse group of healthcare workers wearing face masks" style="left:0;top:0;width:565px;height:558px;background:linear-gradient(180deg,#8a9aa8 0%,#4e7d86 45%,#2a6e73 70%,#2b5f8f 100%)"></div>
  <h2 class="abs" style="left:63px;top:508px;font-weight:700;font-size:17px;line-height:21px;color:var(--white);text-transform:uppercase">Lorem Ipsum Dolor Sit Amet<br>Consectetuer Adipiscing</h2>
  <div class="abs" style="left:0;top:558px;width:565px;height:242px;background:var(--blue)"></div>
  <p class="body light abs" style="left:63px;top:578px;width:212px;height:164px">Lorem ipsum dolor sit amet, consect adipiscing elit, sed diam nonummy nibh euismod tincidunt ut laoreet dol magna aliquam erat volutpat. Ut wisi enim ad minim veniam, quis nostrud exerci tation ullamcorper suscipit lob nisl ut aliquip ex ea commodo cons. Duis autem vel eum iriure dolor inum hendrerit in vulputate velit esse mole consequat, vel illum dolore eu feugia nulla facilisis at vero eros et accums et iusto odio dignissim qui blandit pr</p>
  <p class="body light abs" style="left:318px;top:578px;width:212px;height:164px">Lorem ipsum dolor sit amet, consect adipiscing elit, sed diam nonummy nibh euismod tincidunt ut laoreet dol magna aliquam erat volutpat. Ut wisi enim ad minim veniam, quis nostrud exerci tation ullamcorper suscipit lob nisl ut aliquip ex ea commodo cons. Duis autem vel eum iriure dolor inum hendrerit in vulputate velit esse mole consequat, vel illum dolore eu feugia nulla facilisis at vero eros et accums et iusto odio dignissim qui blandit pr</p>
</section>

<!-- Spread 4 right -->
<section class="page" style="left:600px;top:3441px">
  <h2 class="section-title" style="left:62px;top:62px">Lorem Ipsum Dolor Sit Amet</h2>
  <div class="col" style="left:62px;top:112px;width:205px">
    <h3 class="head">Lorem Ipsum Dolor Sit<br>Amet Consectetuer</h3>
    <p class="body" style="height:258px">Lorem ipsum dolor sit amet, consect adipiscing elit, sed diam nonummy nibh euismod tincidunt ut laoreet dol magna aliquam erat volutpat. Ut wisi enim ad minim veniam, quis nostrud exerci tation ullamcorper suscipit lob nisl ut aliquip ex ea commodo cons. Duis autem vel eum iriure dolor inum hendrerit in vulputate velit esse mole consequat, vel illum dolore eu feugia nulla facilisis at vero eros et accums et iusto odio dignissim qui blandit pr luptatum zzril delenit augue duis dol te feugait nulla facilisi. Lorem ipsum dolor sit amet, cons ectetuer adipisci elit, sed diam nonummy nibh euismo tincidunt ut laoreet dolore magna ali erat volutpat. Ut wisi enim ad minim veniam, quis nostrud exerci tation ull</p>
  </div>
  <div class="abs" style="left:290px;top:117px;width:211px;height:294px;background:var(--blue);padding:26px 20px 0 26px">
    <h3 class="head light">Lorem Ipsum Dolor Sit<br>Amet Consectetuer</h3>
    <ul class="arrows">
      <li>Lorem ipsum dolor sit amet consect adipiscing elit sedia</li>
      <li>Lorem ipsum dolor sit amet consect adipiscing elit sedia</li>
      <li>Lorem ipsum dolor sit amet consect adipiscing elit sedia</li>
      <li>Lorem ipsum dolor sit amet consect adipiscing elit sedia</li>
      <li>Lorem ipsum dolor sit amet consect adipiscing elit sedia</li>
      <li>Lorem ipsum dolor sit amet consect adipiscing elit sedia</li>
    </ul>
  </div>
  <div class="photo" role="img" aria-label="Human hand and robotic hand reaching toward a glowing light" style="left:62px;top:448px;width:439px;height:291px;background:radial-gradient(circle at 55% 45%,#ffffff 0%,#c6d8f2 35%,#7ea3da 75%,#5a86cc 100%)"></div>
</section>

</body>
</html>
```